User-interface and web design for new forum-style communication platform

We developed a new forum-style communication platform specially targetting stock investors to share and discuss information on companies listed on the stock exchange.

You have complete freedom for designing the user-interface and web design. Designs should include all features listed below.

Please read the attached document for full specifications. Also attached is a mockup of the layout, but this is only directional. A mockup for the user-profile is also attached, but does not need to be designed.

This project focusses on the homepage and thread view.

The winner(s) will be asked to design the complete project. (create thread box, user profile, registering, settings...)

We are looking for a well thought out, smart design that incorporates the specifications in the attached document. Please do not hesitate to contact us if anything is not clear.

Target Market(s)

Stock investors from 25 to 60 years old (the people that are currently on investor forums)

Industry/Entity Type

Communication

Font styles to use
Sans Serif

Colors

Designer to choose colors to be used in the design.

Requirements
Must have
• Full homepage design & Thread view specified in the attached document.
Nice to have
• Create thread view
- Field for adding tags
- field for subject of the thread
- text box with basic text editing
- method for sharing media
Should not have
• Logo design.

```html
<!DOCTYPE html>
<html lang="en">
<head>
<meta charset="utf-8">
<title>Investor Forum – Conversations</title>
<link rel="stylesheet" href="https://fonts.googleapis.com/css2?family=Open+Sans:ital,wght@0,400;0,600;0,700;1,400&family=Cousine:wght@400;700&family=Tinos&display=swap">
<style>
:root{
  --page:#f4f4f4;
  --panel:#fafafa;
  --white:#ffffff;
  --dark:#403d3e;
  --ink:#2b2b2b;
  --muted:#888888;
  --line:#d6d6d6;
  --accent:#0a8ac8;
  --link:#0d5a86;
  --btn-grey:#e4e4e4;
}
*{box-sizing:border-box;margin:0;padding:0}
html,body{width:1200px;height:1000px;overflow:hidden}
body{background:var(--page);font-family:"Open Sans",sans-serif;color:var(--ink);position:relative}
.abs{position:absolute}

.company-name{left:116px;top:75px;font-size:15px;color:#333}

.search{left:317px;top:41px;width:469px;height:38px;display:flex;border:1px solid var(--line);background:var(--white)}
.search-field{flex:1;display:flex;align-items:center;gap:10px;padding-left:10px;font-size:13.5px;font-style:italic;color:var(--muted);border:2px solid #e2e2e2;white-space:nowrap}
.search-btn{width:101px;display:flex;align-items:center;justify-content:center;font-size:14px;border-left:1px solid var(--line);background:#f7f7f7}
.search-btn.clear{width:92px;background:var(--btn-grey)}

.badge{left:978px;top:43px;width:37px;height:37px;border-radius:50%;background:var(--accent);border:2px solid #fff;color:#fff;font-family:"Tinos",serif;font-size:27px;display:flex;align-items:center;justify-content:center;box-shadow:0 0 0 1px #cfcfcf;z-index:2}
.user-menu{left:1025px;top:41px;width:88px;height:37px;border:1px solid #ddd;border-radius:19px;background:#f8f8f8;font-family:"Tinos",serif;font-size:15px;display:flex;align-items:center;padding-left:12px;gap:12px}

.notice{left:805px;top:96px;width:210px;background:var(--white);border:1px solid var(--line);font-size:13px}
.notice div{height:42px;display:flex;align-items:center;padding-left:23px;white-space:nowrap}
.notice div+div{border-top:1px solid var(--line);height:41px}

.sidebar{left:70px;top:159px;width:238px}
.side-head{background:var(--dark);color:#fff;font-size:16px;height:34px;display:flex;align-items:center;padding-left:8px;justify-content:space-between;padding-right:8px}
.side-head.serif{font-family:"Tinos",serif;font-size:17px}
.user-search{margin:5px 1px 8px 5px;height:37px;border:2px solid #ddd;background:#fff;display:flex;align-items:center;gap:14px;padding-left:6px;font-size:13px;font-style:italic;color:var(--muted)}
.side-list{background:var(--panel);list-style:none;padding:9px 0 0 5px;position:relative}
.side-list li{height:30px;display:flex;align-items:center;gap:3px;font-size:14px}
.show-all{position:absolute;right:1px;background:var(--dark);color:#fff;font-size:14px;height:27px;display:flex;align-items:center;justify-content:space-between;padding:0 2px 0 12px;white-space:nowrap;line-height:1}
.contributors{background:var(--white);padding:12px 8px 18px;font-family:"Cousine",monospace;font-weight:700;font-size:13px;letter-spacing:-0.6px;color:var(--link);line-height:17px;white-space:nowrap}
.contributors span{color:var(--ink);font-weight:400}

.crumbs{left:355px;top:151px;font-size:14px;display:flex;align-items:center;gap:6px;color:#444;white-space:nowrap}
.crumbs a{color:var(--accent);text-decoration:none;font-weight:600}

.tabs{left:343px;top:184px;height:41px;border:1px solid #ccc;border-radius:21px;background:#f4f4f4;display:flex;font-size:14px}
.tab{display:flex;align-items:center;padding:0 14px;border-left:1px solid #ccc}
.tab.active{background:var(--accent);color:#fff;border-radius:21px 0 0 21px;padding:0 16px 0 25px;border:none}
.tab.last{padding:0 20px}
.tab-pointer{left:418px;top:208px;z-index:6}
.tab-menu{left:376px;top:232px;width:131px;background:#fff;border:1px solid var(--line);box-shadow:0 2px 4px rgba(0,0,0,.15);font-size:13.5px;z-index:5}
.tab-menu div{height:41px;display:flex;align-items:center;justify-content:center}
.tab-menu div+div{border-top:1px solid var(--line);height:40px}
.cursor{left:482px;top:259px;z-index:7}

.new-thread{width:171px;height:35px;border-radius:18px;background:var(--dark);color:#fff;font-size:12.5px;display:flex;align-items:center;gap:9px;padding-left:13px;white-space:nowrap}

.thread{left:355px;top:292px;width:733px;height:207px;border:1px solid #ddd;background:#fff;z-index:1}
.author{position:absolute;left:0;top:0;width:146px;height:206px;background:var(--dark);color:#fff;text-align:center;font-size:12px}
.avatar{width:70px;height:70px;border-radius:50%;background:radial-gradient(circle at 50% 40%,#f2f2f2,#bdbdbd);border:2px solid #e8e8e8;margin:0 auto}
.author .avatar{margin-top:32px}
.author p{margin-top:10px}
.thread-title{position:absolute;left:152px;top:4px;width:576px;height:34px;border:1px solid #ccc;font-size:12px;display:flex;align-items:center;padding-left:15px}
.posted{position:absolute;right:6px;font-size:12px;white-space:nowrap}
.posted b{color:var(--link)}
.thread-body{position:absolute;left:162px;top:53px;font-size:12px;line-height:14.5px;white-space:nowrap}
.thread-meta{position:absolute;left:161px;top:180px;font-size:12px;display:flex;gap:16px;white-space:nowrap}
.thread-meta b{color:var(--link);font-size:13px}
.actions{position:absolute;right:5px;top:169px;display:flex;gap:1px}
.actions div{background:var(--dark);color:#fff;font-size:12px;height:28px;display:flex;align-items:center;padding:0 13px}

.reply{left:503px;top:508px;width:586px;height:126px;border:1px solid #ddd;background:#fff}
.reply .avatar{position:absolute;left:18px;top:12px}
.reply-name{position:absolute;left:0;width:108px;top:90px;text-align:center;font-size:12px}
.reply-rule{position:absolute;left:109px;top:4px;height:118px;border-left:1px dashed #aaa}
.reply-text{position:absolute;left:122px;top:40px;font-family:"Cousine",monospace;font-size:11px;letter-spacing:0.35px;line-height:14.5px;color:#333;white-space:nowrap}

.go-up{left:1002px;top:893px;font-size:27px;color:var(--dark);letter-spacing:-1px;display:flex;align-items:center;gap:12px}
.go-up b{font-weight:700}
.footer{left:70px;top:924px;width:1053px;height:76px;background:var(--dark);color:#fff;font-size:13px;display:flex;align-items:center;justify-content:center}
</style>
</head>
<body>

<div class="abs company-name">Company name</div>

<div class="abs search">
  <div class="search-field">
    <svg width="16" height="16" viewBox="0 0 16 16"><circle cx="6.5" cy="6.5" r="4.5" fill="none" stroke="#aaa" stroke-width="2"/><path d="M10 10l4 4" stroke="#aaa" stroke-width="2.5"/></svg>
    #investement #stockexchange
  </div>
  <div class="search-btn">Save</div>
  <div class="search-btn clear">Clear</div>
</div>

<div class="abs badge">3</div>
<svg class="abs" style="left:990px;top:78px;z-index:3" width="20" height="20" viewBox="0 0 20 20"><path d="M2 0L14 18L12 0Z" fill="#fff" stroke="#cfcfcf"/></svg>
<div class="abs user-menu">USER
  <svg width="10" height="6" viewBox="0 0 10 6"><path d="M0 0h10L5 6z" fill="#333"/></svg>
</div>

<div class="abs notice">
  <div>You have 2 new followers.</div>
  <div>You have 1 new reply.</div>
</div>

<aside class="abs sidebar">
  <div class="side-head">Users
    <svg width="16" height="30" viewBox="0 0 16 30"><circle cx="8" cy="5" r="4.5" fill="#fff"/><rect x="1" y="11" width="14" height="13" rx="3" fill="#fff"/><rect x="3" y="20" width="4" height="10" fill="#fff"/><rect x="9" y="20" width="4" height="10" fill="#fff"/></svg>
  </div>
  <div class="user-search">
    <svg width="16" height="16" viewBox="0 0 16 16"><circle cx="6.5" cy="6.5" r="4.5" fill="none" stroke="#aaa" stroke-width="2"/><path d="M10 10l4 4" stroke="#aaa" stroke-width="2.5"/></svg>
    Type here the username
  </div>

  <div class="side-head">Saved filters</div>
  <ul class="side-list" style="height:213px">
    <li><svg width="16" height="16" viewBox="0 0 16 16"><rect width="16" height="16" fill="#403d3e"/><path d="M2 3h12L9.5 8.5V14L6.5 12V8.5Z" fill="#fff"/></svg>Item 1</li>
    <li><svg width="16" height="16" viewBox="0 0 16 16"><rect width="16" height="16" fill="#403d3e"/><path d="M2 3h12L9.5 8.5V14L6.5 12V8.5Z" fill="#fff"/></svg>Item 2</li>
    <li><svg width="16" height="16" viewBox="0 0 16 16"><rect width="16" height="16" fill="#403d3e"/><path d="M2 3h12L9.5 8.5V14L6.5 12V8.5Z" fill="#fff"/></svg>Item3</li>
    <li><svg width="16" height="16" viewBox="0 0 16 16"><rect width="16" height="16" fill="#403d3e"/><path d="M2 3h12L9.5 8.5V14L6.5 12V8.5Z" fill="#fff"/></svg>Item 4</li>
    <li><svg width="16" height="16" viewBox="0 0 16 16"><rect width="16" height="16" fill="#403d3e"/><path d="M2 3h12L9.5 8.5V14L6.5 12V8.5Z" fill="#fff"/></svg>Item 5</li>
    <li><svg width="16" height="16" viewBox="0 0 16 16"><rect width="16" height="16" fill="#403d3e"/><path d="M2 3h12L9.5 8.5V14L6.5 12V8.5Z" fill="#fff"/></svg>Item 6</li>
    <div class="show-all" style="top:186px;width:97px">show all
      <svg width="26" height="24" viewBox="0 0 26 24"><path d="M0 1h26L16 12V24L10 20V12Z" fill="#fff"/></svg>
    </div>
  </ul>

  <div class="side-head serif" style="margin-top:10px">Popular tags</div>
  <ul class="side-list" style="height:220px;padding-top:9px">
    <li><svg width="15" height="15" viewBox="0 0 15 15"><rect width="15" height="15" fill="#403d3e"/><path d="M5.5 2.5L4.5 12.5M10.5 2.5L9.5 12.5M2.5 5.5h10M2 9.5h10" stroke="#fff" stroke-width="1.4"/></svg>StockExchange</li>
    <li><svg width="15" height="15" viewBox="0 0 15 15"><rect width="15" height="15" fill="#403d3e"/><path d="M5.5 2.5L4.5 12.5M10.5 2.5L9.5 12.5M2.5 5.5h10M2 9.5h10" stroke="#fff" stroke-width="1.4"/></svg>Charting</li>
    <li><svg width="15" height="15" viewBox="0 0 15 15"><rect width="15" height="15" fill="#403d3e"/><path d="M5.5 2.5L4.5 12.5M10.5 2.5L9.5 12.5M2.5 5.5h10M2 9.5h10" stroke="#fff" stroke-width="1.4"/></svg>SavingTips</li>
    <li><svg width="15" height="15" viewBox="0 0 15 15"><rect width="15" height="15" fill="#403d3e"/><path d="M5.5 2.5L4.5 12.5M10.5 2.5L9.5 12.5M2.5 5.5h10M2 9.5h10" stroke="#fff" stroke-width="1.4"/></svg>PayrollJobs_up</li>
    <li><svg width="15" height="15" viewBox="0 0 15 15"><rect width="15" height="15" fill="#403d3e"/><path d="M5.5 2.5L4.5 12.5M10.5 2.5L9.5 12.5M2.5 5.5h10M2 9.5h10" stroke="#fff" stroke-width="1.4"/></svg>StockMarketIndex</li>
    <li><svg width="15" height="15" viewBox="0 0 15 15"><rect width="15" height="15" fill="#403d3e"/><path d="M5.5 2.5L4.5 12.5M10.5 2.5L9.5 12.5M2.5 5.5h10M2 9.5h10" stroke="#fff" stroke-width="1.4"/></svg>YieldUp</li>
    <div class="show-all" style="top:194px;width:97px">show all
      <svg width="18" height="20" viewBox="0 0 18 20"><path d="M6.5 1L4.5 19M13.5 1L11.5 19M1 6.5h16M0 13.5h16" stroke="#fff" stroke-width="2.2"/></svg>
    </div>
  </ul>

  <div class="side-head" style="margin-top:10px">Popular contributors</div>
  <div class="contributors">Frank32<span>, </span>Robert1<span>, </span>Adam<span>, </span>neil<span>,</span><br>investor0<span>, </span>JohnFTT<span>, </span>James312</div>
</aside>

<nav class="abs crumbs">
  <a>Home</a><svg width="5" height="8"><path d="M0 0l5 4-5 4z" fill="#333"/></svg>
  <a>Conversations</a><svg width="5" height="8" style="margin:0 4px"><path d="M0 0l5 4-5 4z" fill="#333"/></svg>
  <a>Public</a><svg width="5" height="8" style="margin:0 4px"><path d="M0 0l5 4-5 4z" fill="#333"/></svg>
  <span>#northwind#lumora</span>
</nav>

<div class="abs tabs">
  <div class="tab active">Public</div>
  <div class="tab" style="border-left:none;padding-left:23px">Following</div>
  <div class="tab last">Contacts</div>
</div>
<svg class="abs tab-pointer" width="30" height="26" viewBox="0 0 30 26"><path d="M1 0L15 25H29Z" fill="#fff" stroke="#d6d6d6"/><path d="M3 3L16 26H28" fill="#fff"/></svg>
<div class="abs tab-menu">
  <div>Recent</div>
  <div>Popular</div>
</div>
<svg class="abs cursor" width="14" height="20" viewBox="0 0 14 20"><path d="M1 1V16L5 12L8 19L10 18L7 11H12Z" fill="#fff" stroke="#555"/></svg>

<div class="abs new-thread" style="left:917px;top:246px">
  <svg width="20" height="20" viewBox="0 0 20 20"><circle cx="10" cy="10" r="9" fill="none" stroke="#fff" stroke-width="1.5"/><path d="M10 5v10M5 10h10" stroke="#fff" stroke-width="1.8"/></svg>
  Create new thread
</div>

<article class="abs thread">
  <div class="author">
    <div class="avatar" role="img" aria-label="Profile picture of Frank32"></div>
    <p>Frank32</p>
  </div>
  <div class="thread-title">Buying investment property - How to?</div>
  <div class="posted" style="top:41px">Posted by <b>Frank32</b> on 30/03/2014 - 05:32</div>
  <div class="thread-body">
    Hello everyone,<br><br>
    So i am new here and i am interested in buying some property where i can invest<br>
    Before i do that i need some opinions on how to do that so i won't make mistakes.<br>
    Maybe you can tell me some cites where i can find what i am looking for.<br>
    I want to be prepared very good before i start my first investment.<br><br>
    Thanks
  </div>
  <div class="thread-meta"><b>Read more</b><span>1 reply</span><span>25 views</span></div>
  <div class="actions"><div>Reply</div><div>Share</div><div>Favourite</div></div>
</article>

<article class="abs reply">
  <div class="avatar" role="img" aria-label="Profile picture of Robert1"></div>
  <div class="reply-name">Robert1</div>
  <div class="reply-rule"></div>
  <div class="posted" style="top:6px">Posted by <b>Robert1</b> on 30/03/2014 - 07:32</div>
  <p class="reply-text">Some are saying we're in another real estate bubble... some<br>are saying the sky is the limit.... it all depends on your outlook<br>on the economy. You could invest in REIT stocks that pay 90%<br>of their profits in dividends</p>
</article>

<div class="abs new-thread" style="left:920px;top:649px">
  <svg width="20" height="20" viewBox="0 0 20 20"><circle cx="10" cy="10" r="9" fill="none" stroke="#fff" stroke-width="1.5"/><path d="M10 5v10M5 10h10" stroke="#fff" stroke-width="1.8"/></svg>
  Create new thread
</div>

<div class="abs go-up"><span>GO<b>UP</b></span>
  <svg width="10" height="22" viewBox="0 0 10 22"><path d="M5 0L9 6H6V22H4V6H1Z" fill="#403d3e"/></svg>
</div>

<footer class="abs footer">© YourCompanyName.com | 2014</footer>

</body>
</html>
```